New business card for my lawn and landscape business

Hollin Yard and Building is a full-service lawn care, landscaping, and light construction company serving Paragould and the Northeast Arkansas region. The business is owned and operated by Dorian Waltham, with a reputation for hands-on, detail-oriented service, dependable crews, and quality results for both residential and commercial clients. A well regarded business with great reviews.
Owner Dorian Waltham
Hollinyardandbuilding.example

Target Market(s)

Commercial, Middle, and upper class in north east Arkansas

Industry/Entity Type

Lawn maintenance and landscape

Contact Information for Business Card

Hollin Yard And Building Professional lawn care, landscaping, and property improvement in Northeast Arkansas. • lawn maintenance •lawn treatments and weed control • exterior projects • Custom landscape design & installation • Sod, trees, rock & drainage solutions • Residential & commercial services Reliable. Detailed. Done right.

Requirements
Must have
• Business name, service area, list of some of our services, clean design that represents
Nice to have
• Unique. Different design element than just grass because its already in n the logo. Picture of a warm season (south) lawn or landscape. Pictures of the type of work we do

```html
<!DOCTYPE html>
<html lang="en">
<head>
<meta charset="utf-8">
<title>Hollin Yard and Building — Business Card</title>
<link href="https://fonts.googleapis.com/css2?family=Montserrat:wght@600;700&family=Crimson+Text:wght@400;600&display=swap" rel="stylesheet">
<style>
  :root {
    --backdrop: #2b2b2d;
    --card: #ffffff;
    --card-shade: #ececec;
    --green: #6ab033;
    --green-deep: #56982a;
    --ink: #3a3a3a;
    --grey: #8a8a8c;
  }
  * { margin: 0; padding: 0; box-sizing: border-box; }
  html, body {
    width: 1200px; height: 900px; overflow: hidden;
    background: var(--backdrop);
  }
  .stage { position: relative; width: 1200px; height: 900px; }
  .card {
    position: absolute;
    width: 580px; height: 332px;
    background: linear-gradient(160deg, var(--card) 40%, var(--card-shade) 100%);
    overflow: hidden;
    box-shadow: 0 10px 24px rgba(0,0,0,.45);
  }
  .card--back { left: 90px; top: 80px; }
  .card--front { left: 530px; top: 488px; }
  .card__band {
    position: absolute; left: 0; right: 0; bottom: 0; height: 16px;
    background: var(--green);
  }
  .card__lawn {
    position: absolute; bottom: 16px; height: 86px;
    background: linear-gradient(180deg, rgba(106,176,51,0) 0%, var(--green) 70%);
  }
  .card--back .card__lawn { left: 110px; width: 190px; }
  .card--front .card__lawn { right: 0; width: 200px; }

  .brand {
    position: absolute; display: flex; align-items: center; gap: 10px;
    font-family: "Montserrat", sans-serif; font-weight: 700;
    color: var(--green); font-size: 19px; line-height: 1.15;
    text-transform: uppercase; letter-spacing: .5px;
  }
  .brand__dot {
    width: 54px; height: 54px; border-radius: 50%;
    border: 6px solid var(--grey); flex: none;
  }
  .card--back .brand { right: 30px; top: 86px; width: 230px; }
  .card--front .brand { right: 24px; top: 40px; width: 230px; }

  .services {
    position: absolute; left: 34px; top: 64px;
    font-family: "Crimson Text", serif; color: var(--ink);
  }
  .services__title {
    font-weight: 600; color: var(--green); font-size: 20px;
    text-transform: uppercase; letter-spacing: .3px; margin-bottom: 2px;
  }
  .services__list { list-style: none; font-size: 15.5px; line-height: 1.32; }
  .services__list li::before {
    content: "•"; color: var(--green); margin-right: 8px; margin-left: 8px;
  }

  .owner { position: absolute; left: 40px; top: 178px; }
  .owner__name {
    font-family: "Montserrat", sans-serif; font-weight: 700;
    color: var(--green); font-size: 22px; text-transform: uppercase;
    letter-spacing: -.3px;
  }
  .owner__role {
    font-family: "Crimson Text", serif; color: var(--ink); font-size: 16px;
    margin-top: -4px;
  }
  .contacts {
    list-style: none; margin-top: 14px;
    font-family: "Crimson Text", serif; color: var(--ink); font-size: 16px;
  }
  .contacts li { display: flex; align-items: center; gap: 9px; line-height: 1.5; }
  .contacts svg { width: 14px; height: 14px; flex: none; }
</style>
</head>
<body>
<div class="stage">

  <section class="card card--back" aria-label="Card back: services">
    <div class="services">
      <h2 class="services__title">Our Services</h2>
      <ul class="services__list">
        <li>Lawn Maintenance</li>
        <li>Lawn Treatments And Weed Control</li>
        <li>Exterior Projects</li>
        <li>Custom Landscape Design &amp; Installation</li>
        <li>Sod, Trees, Rock &amp; Drainage Solutions</li>
        <li>Residential &amp; Commercial Services Reliable</li>
      </ul>
    </div>
    <div class="brand"><span class="brand__dot"></span><span>Hollin Yard And Building</span></div>
    <div class="card__lawn" role="img" aria-label="Green grass blades illustration"></div>
    <div class="card__band"></div>
  </section>

  <section class="card card--front" aria-label="Card front: contact">
    <div class="brand"><span class="brand__dot"></span><span>Hollin Yard And Building</span></div>
    <div class="owner">
      <h1 class="owner__name">Dorian Waltham</h1>
      <p class="owner__role">Owner</p>
      <ul class="contacts">
        <li>
          <svg viewBox="0 0 24 24" aria-hidden="true"><path fill="var(--green)" d="M6.6 10.8a15 15 0 0 0 6.6 6.6l2.2-2.2c.3-.3.7-.4 1-.2 1.1.4 2.3.6 3.6.6.6 0 1 .4 1 1V20c0 .6-.4 1-1 1A17 17 0 0 1 3 4c0-.6.4-1 1-1h3.5c.6 0 1 .4 1 1 0 1.3.2 2.5.6 3.6.1.3 0 .7-.2 1z"/></svg>
          (555) 214-0186
        </li>
        <li>
          <svg viewBox="0 0 24 24" aria-hidden="true"><path fill="var(--green)" d="M12 2a7 7 0 0 0-7 7c0 5.2 7 13 7 13s7-7.8 7-13a7 7 0 0 0-7-7zm0 9.5A2.5 2.5 0 1 1 12 6.5a2.5 2.5 0 0 1 0 5z"/></svg>
          Marrowvale, ZX 00450
        </li>
        <li>
          <svg viewBox="0 0 24 24" aria-hidden="true"><g fill="none" stroke="var(--green)" stroke-width="1.8"><circle cx="12" cy="12" r="9"/><path d="M3 12h18M12 3c3 3 3 15 0 18M12 3c-3 3-3 15 0 18"/></g></svg>
          Hollinyardandbuilding.example
        </li>
      </ul>
    </div>
    <div class="card__lawn" role="img" aria-label="Green grass blades illustration"></div>
    <div class="card__band"></div>
  </section>

</div>
</body>
</html>
```